Etikett für Bierflaschen
Anforderungen:
Bitte entwerfen Sie Etiketten für Bierflaschen (Bügelflaschen), welches man ggf. auch als Logo für eine kleine Hausbrauerei benutzen kann.
Der Bezug zur Region sollte erkennbar sein. (Norddeutschland/Teufelsmoor).
Gut wäre, wenn eine Torfkahn-Zeichnung enthalten wäre.
Im Vorder-Etikett sollte der Name der Brauerei (Kranwieder Hausbrauerei), der Biername (58er) und der Biertyp (Bsp.Pilsener), haltbar bis,Vol% zu sehen sein.
Im hinteren Etikett (Flaschenrückseite) möchte ich das Bier beschreiben und die Inhaltsstoffe angeben. Evtl. könnten auch hier haltbar bis und/oder %vol. stehen. Last but not leased hat die Bügelflasche noch ein Etikett am Hals,
Unternehmensbeschreibung:
Hierbei handelt es sich um eine kleine Hausbrauerei, die noch nicht gegründet ist. Wichtig für den Vertrieb des Bieres ist der Bezug zur Region
Norddeutschland,Teufelsmoor,Torfkahn) Das Bier wird nicht in großen Mengen hergestellt. Vorgesehen sind kleinere Fässer und 1-Liter und 2-Literflaschen.
Zielgruppe:
Von jung bis alt.
Farben, Logo-Favoriten und weitere Anforderungen
Nur eine Idee:
Dunkel-Gelb am Rand (hier könnte der Name der Brauerei geschrieben sein), Der Torfkahn und die Landschaft braun.
Ansonsten hell z.B. grau
Die Bezeichnung des Biertyps könnte man je nach Biertyp in verschiedenen Farben hinterlegen.
Ein Beispiel einer anderen Brauerei (Mit Leuchtturm) ist als Datei beigefügt.
Hallo,
Mit freundlichen Grüßen
die Länge des Halsetiketts soll ca. 7,5cm sein. MfG

```html
<!DOCTYPE html>
<html lang="de">
<head>
<meta charset="utf-8">
<title>58er – Etiketten Kranwieder Hausbrauerei</title>
<link rel="stylesheet" href="https://fonts.googleapis.com/css2?family=Grenze:wght@400;700&family=Audiowide&display=swap">
<style>
  :root {
    --label-dark: #2b2b2b;
    --moor-mint: #9fc4aa;
    --boat-mint: #8cb198;
    --page: #ffffff;
  }
  * { margin: 0; padding: 0; box-sizing: border-box; }
  html, body { width: 1190px; height: 1200px; overflow: hidden; background: var(--page); }
  .sheet { position: relative; width: 1190px; height: 1200px; }

  .label {
    position: absolute;
    background: var(--label-dark);
    border-radius: 16px;
    color: var(--moor-mint);
    font-family: "Grenze", serif;
    overflow: hidden;
  }
  .boat-area {
    position: absolute;
    background: linear-gradient(180deg, var(--moor-mint), var(--boat-mint));
    border-radius: 6px 30px 4px 4px;
  }

  /* Front label */
  .label--front { left: 56px; top: 50px; width: 450px; height: 516px; }
  .label--front .boat-area { left: 178px; top: 110px; width: 100px; height: 170px; }
  .rule { position: absolute; height: 2px; background: var(--moor-mint); }
  .label--front .rule--top { left: 70px; width: 310px; top: 280px; }
  .beer-name {
    position: absolute; left: 0; width: 100%; top: 300px;
    text-align: center; font-weight: 700; font-size: 112px; line-height: 1;
    letter-spacing: 4px;
  }
  .brewery-name {
    position: absolute; left: 0; width: 100%; top: 410px;
    text-align: center; font-size: 31px; letter-spacing: 1px; text-transform: uppercase;
  }
  .beer-type-row {
    position: absolute; left: 30px; right: 30px; top: 470px;
    display: flex; align-items: center; gap: 16px;
  }
  .beer-type-row .line { flex: 1; height: 2px; background: var(--moor-mint); }
  .beer-type {
    font-family: "Audiowide", sans-serif; font-size: 24px; letter-spacing: 2px;
  }

  /* Back labels */
  .label--back-a { left: 696px; top: 50px; width: 448px; height: 516px; }
  .label--back-b { left: 696px; top: 646px; width: 448px; height: 516px; }
  .vertical-name {
    position: absolute; left: 8px; top: 10px;
    writing-mode: vertical-rl;
    font-weight: 700; font-size: 120px; line-height: 1; letter-spacing: 6px;
  }
  .description, .ingredients {
    position: absolute; text-align: center; font-size: 17px; line-height: 25px;
  }
  .label--back-a .description { left: 104px; width: 330px; top: 92px; }
  .label--back-a .ingredients { left: 104px; width: 330px; top: 252px; }
  .label--back-a .boat-area { left: 234px; top: 300px; width: 88px; height: 140px; }
  .facts {
    position: absolute; font-family: "Audiowide", sans-serif; font-size: 13px;
    letter-spacing: 1.5px; line-height: 17px; text-align: center;
  }
  .label--back-a .facts { left: 104px; width: 330px; top: 462px; }

  .label--back-b .description { left: 112px; width: 262px; top: 62px; line-height: 31px; }
  .label--back-b .ingredients { left: 125px; width: 220px; top: 368px; line-height: 31px; }
  .label--back-b .boat-area { left: 344px; top: 346px; width: 84px; height: 148px; }
  .label--back-b .facts {
    right: 16px; top: 30px; text-align: left;
    writing-mode: vertical-rl;
  }

  /* Neck tags */
  .neck-tags { position: absolute; left: 30px; top: 750px; }
  .tag-name-vertical {
    font-family: "Grenze", serif; font-weight: 700; font-size: 44px; letter-spacing: 2px;
  }
  .tag-name-stack {
    font-family: "Grenze", serif; font-weight: 700; font-size: 30px;
  }
</style>
</head>
<body>
<main class="sheet">

  <section class="label label--front" aria-label="Vorderetikett">
    <div class="boat-area" role="img" aria-label="Torfkahn mit Segel"></div>
    <div class="rule rule--top"></div>
    <h1 class="beer-name">58er</h1>
    <p class="brewery-name">Kranwieder Hausbrauerei</p>
    <div class="beer-type-row">
      <span class="line"></span>
      <span class="beer-type">PILSENER</span>
      <span class="line"></span>
    </div>
  </section>

  <section class="label label--back-a" aria-label="Rückenetikett, Variante 1">
    <div class="vertical-name">58er</div>
    <p class="description">Dieses untergärige Bier ist handwerklich gebraut und naturbelassen mit Zutaten aus der Region. Wertvolle Geschmacks- und gesundheitsfördernde Inhaltsstoffe werden nicht ausgefiltert, was dem Bier sein naturtrübes Aussehen verleiht.</p>
    <p class="ingredients">Zutaten: Wasser, Malz, feiner Hopfen</p>
    <div class="boat-area" role="img" aria-label="Torfkahn mit Segel"></div>
    <p class="facts">ALC. 4.5% - 2 L<br>BEST BEFORE : 22.04.2014</p>
  </section>

  <section class="label label--back-b" aria-label="Rückenetikett, Variante 2">
    <div class="vertical-name">58er</div>
    <p class="description">Dieses untergärige Bier ist<br>handwerklich gebraut und<br>naturbelassen mit Zutaten<br>aus der Region.<br>Wertvolle Geschmacks und<br>gesundheitsfördernde<br>Inhaltsstoffe werden nicht<br>ausgefiltert, was dem Bier sein<br>naturtrübes Aussehen verleiht.</p>
    <p class="ingredients">Zutaten :<br>Wasser<br>Malz<br>feiner Hopfen</p>
    <div class="boat-area" role="img" aria-label="Torfkahn mit Segel"></div>
    <p class="facts">ALC. 4.5% - 2 L<br>BEST BEFORE : 22.04.14</p>
  </section>

  <svg class="neck-tags" width="520" height="280" viewBox="0 0 520 280" aria-label="Halsetiketten">
    <g>
      <circle cx="56" cy="50" r="44" fill="var(--label-dark)"/>
      <rect x="26" y="50" width="60" height="216" rx="30" fill="var(--label-dark)"/>
      <rect x="42" y="18" width="28" height="50" rx="4" fill="var(--moor-mint)" role="img" aria-label="Torfkahn"/>
      <text class="tag-name-vertical" x="56" y="90" fill="var(--moor-mint)" transform="rotate(90 56 90)" dominant-baseline="middle">58er</text>
    </g>
    <g>
      <circle cx="184" cy="50" r="44" fill="var(--moor-mint)"/>
      <rect x="154" y="50" width="60" height="216" rx="30" fill="var(--moor-mint)"/>
      <rect x="170" y="18" width="28" height="50" rx="4" fill="var(--label-dark)" role="img" aria-label="Torfkahn"/>
      <text class="tag-name-vertical" x="184" y="90" fill="var(--label-dark)" transform="rotate(90 184 90)" dominant-baseline="middle">58er</text>
    </g>
    <g>
      <circle cx="316" cy="50" r="44" fill="var(--label-dark)"/>
      <rect x="296" y="50" width="40" height="160" fill="var(--label-dark)"/>
      <circle cx="316" cy="214" r="48" fill="var(--label-dark)"/>
      <rect x="302" y="18" width="28" height="50" rx="4" fill="var(--moor-mint)" role="img" aria-label="Torfkahn"/>
      <line x1="316" y1="88" x2="316" y2="160" stroke="var(--moor-mint)" stroke-width="3"/>
      <text class="tag-name-stack" x="316" y="224" fill="var(--moor-mint)" text-anchor="middle">58er</text>
    </g>
    <g>
      <circle cx="448" cy="50" r="44" fill="var(--moor-mint)"/>
      <rect x="428" y="50" width="40" height="160" fill="var(--moor-mint)"/>
      <circle cx="448" cy="214" r="48" fill="var(--moor-mint)"/>
      <rect x="434" y="18" width="28" height="50" rx="4" fill="var(--label-dark)" role="img" aria-label="Torfkahn"/>
      <line x1="448" y1="88" x2="448" y2="160" stroke="var(--label-dark)" stroke-width="3"/>
      <text class="tag-name-stack" x="448" y="224" fill="var(--label-dark)" text-anchor="middle">58er</text>
    </g>
  </svg>

</main>
</body>
</html>
```